Electrical Product Brochure Design

We have 15 electricians on the road and want to create a product brochure for them to show residential clients. I have attached all the product images in high res to be used and some images of our company and logo. I have also attached a previous product brochure that was designed which we don't want to use/has been edited. Additionally there is a Word document with the content that is needed.

Please create the brochure as a double sided A4 brochure.
Updates

Hi, Thank you for your designs. Please see the updated brief including ensuring the design is a double sided A4 flyer. Please ensure all products from the product brochure content are used on the design and all content. Please ensure Travik's contact information is used as well. Please ensure you see the updated brief for new product images I have now been able to upload as well as a few options for images of our tradespeople that can be used. Thank you.

Target Market(s)

Homeowners

Industry/Entity Type

Electrical

Font styles to use
Sans Serif

Colors
0255a3
fbed22
ec1f27

Requirements
Must have
• Travik colours including mainly blue, but also red and a bit of yellow.
• Travik's contact information including website, phone, email, and PO Box address.
• Each product's image with the content listed next to the image.
Nice to have
• If the four types of fan images could be used, and listed as one product.
• If you could also use images of our tradespeople attached as well?

```html
<!DOCTYPE html>
<html lang="en">
<head>
<meta charset="utf-8">
<title>Travik Electrical Services – Product Flyer</title>
<link href="https://fonts.googleapis.com/css2?family=Oswald:wght@400&family=Roboto:wght@400;500&display=swap" rel="stylesheet">
<style>
:root{
  --brand-blue:#1a4f9e;
  --title-blue:#1f3fae;
  --stripe-blue:#4a86d0;
  --navy:#16238f;
  --page-bg:#eef0f3;
  --text:#2b2b2b;
  --canvas-bg:#d4d8dd;
}
*{margin:0;padding:0;box-sizing:border-box}
html,body{width:1200px;height:965px;overflow:hidden;background:var(--canvas-bg)}
.canvas{position:relative;width:1200px;height:965px}
.page{position:absolute;top:50px;width:704px;height:995px;background:var(--page-bg);transform:scale(.8);transform-origin:0 0;overflow:hidden;font-family:"Roboto",Arial,sans-serif;color:var(--text)}
.page--front{left:21px}
.page--back{left:616px}
.page svg.shapes{position:absolute;left:0;top:0}
.brand{position:absolute;left:158px;top:10px;width:200px;text-align:center;font-family:"Oswald",sans-serif;font-size:30px;letter-spacing:4px;color:var(--navy);line-height:1.05}
.brand small{display:block;font-size:13px;letter-spacing:1.5px}
.product{position:absolute;width:235px}
.product h2{font-family:"Oswald",sans-serif;font-weight:400;font-size:14.5px;color:var(--title-blue);line-height:17px}
.product .sub{font-size:9px;color:var(--title-blue);margin-top:1px}
.product h3{font-size:11.5px;font-weight:500;margin-top:6px;line-height:13px}
.product ul{list-style:none;font-size:8.8px;line-height:11.2px}
.product li{padding-left:6px;position:relative;margin-top:2px}
.product li::before{content:"•";position:absolute;left:0}
.col-l{left:14px}
.col-r{left:274px}
.back-title{position:absolute;font-family:"Oswald",sans-serif;font-weight:400;font-size:25px;color:var(--title-blue);white-space:nowrap}
.specs{position:absolute;list-style:none;font-size:9.2px;line-height:13.3px}
.specs li::before{content:"• "}
.photo{position:absolute}
.spec-table{position:absolute;border:2px solid var(--navy);border-collapse:collapse;background:#fff;font-size:7px;color:#222;table-layout:fixed}
.spec-table th{background:#e3e5e8;font-weight:500;text-align:left;padding:2px 4px;height:13px;font-size:7px;white-space:nowrap}
.spec-table td{padding:0 4px;border-top:1px solid #d5d7db;height:22px;white-space:nowrap}
.spec-table td.part{font-weight:500}
.spec-table td.thumb{padding:4px 8px}
.thumb span{display:block;width:54px;height:28px;border-radius:2px}
.thumb .gold{background:linear-gradient(90deg,#a9794f,#e0b48c 30%,#eceef1 60%,#c9ccd1)}
.thumb .black{background:linear-gradient(90deg,#2e2e2e,#6d6d6d 30%,#eceef1 60%,#c9ccd1)}
.contact{position:absolute;left:13px;top:877px;color:#fff;font-size:11px;line-height:15px;width:165px}
.contact h4{font-family:"Oswald",sans-serif;font-weight:400;font-size:16px;margin-bottom:4px}
.contact p{display:flex;gap:6px;align-items:flex-start}
.contact svg{flex:none;margin-top:2px}
</style>
</head>
<body>
<div class="canvas">

<section class="page page--front">
  <svg class="shapes" width="704" height="995" viewBox="0 0 704 995">
    <defs>
      <radialGradient id="g-power" cx=".5" cy=".45" r=".6"><stop offset="0" stop-color="#ffffff"/><stop offset="1" stop-color="#d3d6db"/></radialGradient>
      <radialGradient id="g-alarm" cx=".55" cy=".5" r=".6"><stop offset="0" stop-color="#fbfbfc"/><stop offset=".7" stop-color="#e2e4e8"/><stop offset="1" stop-color="#b9bdc4"/></radialGradient>
      <linearGradient id="g-surge" x1="0" y1="0" x2="1" y2="1"><stop offset="0" stop-color="#f2f2f0"/><stop offset=".6" stop-color="#d9d9d6"/><stop offset="1" stop-color="#b9b9b5"/></linearGradient>
      <radialGradient id="g-heat" cx=".55" cy=".45" r=".65"><stop offset="0" stop-color="#fff4c8"/><stop offset=".5" stop-color="#d8bd6a"/><stop offset="1" stop-color="#8f7a3e"/></radialGradient>
    </defs>
    <polygon points="624,0 704,0 704,995 519,995" fill="var(--brand-blue)"/>
    <polygon points="534,227 548,227 503,995 489,995" fill="var(--stripe-blue)"/>
    <polygon role="img" aria-label="Photo of a four gang power point" points="476,0 552,0 592,67 552,137 476,137 436,67" fill="url(#g-power)" stroke="#fff" stroke-width="4"/>
    <polygon role="img" aria-label="Photo of a photoelectric smoke alarm" points="576,152 652,152 692,224 652,296 576,296 536,224" fill="url(#g-alarm)" stroke="#fff" stroke-width="4"/>
    <polygon role="img" aria-label="Photo of a surge protector module" points="538,381 630,381 676,454 630,528 538,528 492,454" fill="url(#g-surge)" stroke="#fff" stroke-width="4"/>
    <polygon role="img" aria-label="Photo of a four lamp heat vent light" points="470,738 566,738 614,824 566,910 470,910 422,824" fill="url(#g-heat)" stroke="#fff" stroke-width="4"/>
  </svg>

  <div class="brand">TRAVIK<small>ELECTRICAL SERVICES</small></div>

  <div class="product col-l" style="top:80px">
    <h2>USB POWER POINT</h2>
    <h3>Features</h3>
    <ul><li>2 x 2.1 AMP USB sockets for faster charging.</li></ul>
    <h3>Benefits</h3>
    <ul><li>Reduces clutter and bulky chargers.</li><li>You can charge two devices such as your smart phone and tablet at once.</li><li>Don't use up one power point with a charger, more space for other appliances to be plugged in.</li></ul>
  </div>
  <div class="product col-l" style="top:218px">
    <h2>PHOTOELECTRIC SMOKE</h2>
    <div class="sub">(WITH REPLACEABLE BATTERY)</div>
    <h3>Features</h3>
    <ul><li>Battery back up with connection to mains power.</li></ul>
    <h3>Benefits</h3>
    <ul><li>Hush button in case of false alarms.</li><li>Separate mains and warning LED's Photoelectric alarms are responsive to smouldering fires as opposed to flaming fires.</li></ul>
  </div>
  <div class="product col-l" style="top:402px">
    <h2>SURGE PROTECTOR</h2>
    <div class="sub">(SPX165R - SURGE PROTECTOR)</div>
    <h3>Features</h3>
    <ul><li>Protection against unexpected power surges.</li></ul>
    <h3>Benefits</h3>
    <ul><li>Fits easily into your existing switchboard.</li><li>Your appliances are protected against unexpected surges such as those caused by storms.</li></ul>
  </div>
  <div class="product col-l" style="top:542px">
    <h2>CEILING FAN WITH LIGHT &amp; REMOTE</h2>
    <h3>Features</h3>
    <ul><li>Energy efficient when compared with expensive air conditioning costs.</li></ul>
    <h3>Benefits</h3>
    <ul><li>Comes with or without a light.</li><li>Remote control for convenience.</li><li>Can replace existing light fitting.</li></ul>
  </div>
  <div class="product col-l" style="top:670px">
    <h2>LED DOWNLIGHT WITH DIMMABLE DRIVER</h2>
    <h3>Features</h3>
    <ul><li>All in 1 downlight: White, neutral white &amp; warm white.</li><li>Designer finish with slimline lip &amp; recessed face.</li></ul>
    <h3>Benefits</h3>
    <ul><li>No harmful effects.</li><li>Does not overheat.</li><li>Power saving.</li><li>Long lasting - low to no globe maintenance cost.</li><li>Low heat.</li><li>Dimmable.</li><li>Security.</li></ul>
  </div>
  <div class="product col-l" style="top:884px">
    <h2>AIRVANE HEAT VENT LIGHT</h2>
    <div class="sub">(4 HEAT LIGHT)</div>
    <ul style="margin-top:6px"><li>Energy saving.</li><li>4 x heat lamps for instant heat and comfort.</li><li>Powerful extraction to prevent steam and mold build up.</li><li>42W centre light.</li></ul>
  </div>

  <div class="product col-r" style="top:80px">
    <h2>4 GANG POWER POINTS</h2>
    <h3>Features</h3>
    <ul><li>Four power point in one unit.</li></ul>
    <h3>Benefits</h3>
    <ul><li>Neater.</li><li>Great for when you need to plug in multiple devices or appliances.</li></ul>
  </div>
  <div class="product col-r" style="top:218px;width:250px">
    <h2>PHOTOELECTRIC SMOKE ALARM</h2>
    <div class="sub">(WITH 10 YEAR LITHIUM BATTERY)</div>
    <h3>Features</h3>
    <ul><li>Connected to mains power also with a 10 year re-chargeable lithium battery</li></ul>
    <h3>Benefits</h3>
    <ul><li>Hush button for false alarm control.</li><li>Low cell warning in event of mains or cell failure.</li><li>Precision charging circuit ensure peak cell performance.</li><li>No need to change batteries.</li><li>Photoelectric alarms are responsive to smouldering fires as opposed to flaming fires.</li></ul>
  </div>
  <div class="product col-r" style="top:402px">
    <h2>DIMMERS</h2>
    <div class="sub">(DMU450UE – UNIVERSAL DIMMER)</div>
    <h3>Features</h3>
    <ul><li>Adapts lighting to brightness preference.</li></ul>
    <h3>Benefits</h3>
    <ul><li>Creates mood lighting.</li><li>Increases longevity of bulbs.</li><li>Energy saving.</li></ul>
  </div>
  <div class="product col-r" style="top:542px">
    <h2>SECURITY LED TWIN FLOOD</h2>
    <ul style="margin-top:6px"><li>Low heat.</li><li>Long lasting - low to no globe maintenance cost.</li><li>Energy saving.</li><li>Available in black or white.</li></ul>
  </div>
  <div class="product col-r" style="top:670px;width:200px">
    <h2>SECUIRTY LED TWIN SENSOR FLOOD</h2>
    <ul style="margin-top:12px"><li>Detects motion and instantly turns on LED light.</li><li>Timing and lux adjustments.</li><li>Low heat.</li><li>Long lasting.</li><li>Energy saving.</li><li>Available in black or white.</li></ul>
  </div>
  <div class="product col-r" style="top:884px;width:220px">
    <h2>AIRVANE HEAT VENT LIGHT</h2>
    <div class="sub">(2 HEAT LIGHT)</div>
    <ul style="margin-top:6px"><li>Energy saving.</li><li>2 x heat lamps for instant heat and comfort.</li><li>Powerful extraction to prevent steam and mold build up.</li><li>100W centre light.</li></ul>
  </div>
</section>

<section class="page page--back">
  <svg class="shapes" width="704" height="995" viewBox="0 0 704 995">
    <defs>
      <radialGradient id="g-fan" cx=".5" cy=".45" r=".6"><stop offset="0" stop-color="#ffffff"/><stop offset=".7" stop-color="#e6e8eb"/><stop offset="1" stop-color="#c3c7cd"/></radialGradient>
      <radialGradient id="g-flood" cx=".5" cy=".5" r=".6"><stop offset="0" stop-color="#5a5d62"/><stop offset=".55" stop-color="#25272b"/><stop offset="1" stop-color="#d9dbdf"/></radialGradient>
    </defs>
    <polygon points="0,0 86,0 180,995 0,995" fill="var(--brand-blue)"/>
    <polygon points="116,240 130,240 218,995 204,995" fill="var(--stripe-blue)"/>
    <polygon role="img" aria-label="Photo of a white ceiling fan with light" points="56,152 134,152 174,224 134,296 56,296 16,224" fill="url(#g-fan)" stroke="#fff" stroke-width="4"/>
    <polygon role="img" aria-label="Photo of a twin LED sensor flood light" points="68,381 160,381 206,454 160,528 68,528 22,454" fill="url(#g-flood)" stroke="#fff" stroke-width="4"/>
  </svg>

  <h1 class="back-title" style="left:249px;top:8px">GOLD UP / DOWN WALL PILLAR SPOT LIGHT</h1>
  <ul class="specs" style="left:272px;top:74px">
    <li>Up/down wall pillar light.</li><li>Gold coloured aluminium.</li><li>Includes a matching aluminium backing plate</li><li>High output reflector to maximise light.</li><li>240v GU10 2x35w max/12v MR16 2x20w max</li><li>IP rating : IP65</li>
  </ul>
  <div class="photo" role="img" aria-label="Gold up and down wall pillar spot light" style="left:526px;top:48px;width:50px;height:134px;border-radius:4px;background:linear-gradient(90deg,#9c6d45,#e6bc94 45%,#a9794f)"></div>

  <table class="spec-table" style="left:234px;top:202px;width:454px">
    <tr><th style="width:82px;text-align:center">IMAGE</th><th style="width:66px">PART NUMBER</th><th style="width:68px">COLOUR TEMP</th><th style="width:67px">OUTPUT</th><th style="width:66px">POWER</th><th>INCLUDED GLOBES</th></tr>
    <tr><td class="thumb" rowspan="2"><span class="gold" role="img" aria-label="Pillar light with COB globes"></span></td><td class="part">LX1055C</td><td>Cool white, 6000k</td><td>2x 500lm</td><td>240v LED 20w</td><td>2x 10w COB LED globes</td></tr>
    <tr><td class="part">LX1055W</td><td>Warm white, 3000k</td><td>2x 460lm</td><td>240v LED 20w</td><td>2x 10w COB LED globes</td></tr>
    <tr><td class="thumb" style="height:44px"><span class="gold" role="img" aria-label="Pillar light body only"></span></td><td class="part">LX1056</td><td>NA</td><td>NA</td><td>240v GU10<br>2x35w max</td><td>NA</td></tr>
    <tr><td class="thumb" rowspan="2"><span class="gold" role="img" aria-label="Pillar light with GU10 globes"></span></td><td class="part">LX1057GU10C</td><td>Cool white, 6000k</td><td>2x 300lm</td><td>240v LED 10w</td><td>2x 5w LED globes</td></tr>
    <tr><td class="part">LX1057GU10W</td><td>Warm white, 3000k</td><td>2x 250lm</td><td>240v LED 10w</td><td>2x 5w LED globes</td></tr>
    <tr><td class="thumb" rowspan="2"><span class="gold" role="img" aria-label="Pillar light with MR16 globes"></span></td><td class="part">LX1057MR16C</td><td>Cool white, 6000k</td><td>2x 300lm</td><td>12v LED 10w</td><td>2x 5w LED globes</td></tr>
    <tr><td class="part">LX1057MR16W</td><td>Warm white, 3000k</td><td>2x 250lm</td><td>12v LED 10w</td><td>2x 5w LED globes</td></tr>
  </table>

  <h1 class="back-title" style="left:282px;top:428px">MATT BLACK GARDEN SPIKE LIGHTS</h1>
  <ul class="specs" style="left:272px;top:480px">
    <li>Double adjustable spike spotlight.</li><li>Aluminium poly powder coated black.</li><li>Internal cable.</li><li>Spike length : 1000mm.</li><li>2m reinforced cable</li><li>12v MR16 2x20w max.</li><li>IP rating : IP65.</li><li>Can be used with halogen globes.</li><li>Refer to pages 188-192 for suitable LED drivers.</li>
  </ul>
  <div class="photo" role="img" aria-label="Double head black garden spike light" style="left:553px;top:470px;width:24px;height:142px;background:linear-gradient(180deg,#2a2a2a,#4a4a4a 25%,rgba(60,60,60,.5) 60%,rgba(238,240,243,0))"></div>

  <table class="spec-table" style="left:234px;top:622px;width:454px">
    <tr><th style="width:82px;text-align:center">IMAGE</th><th style="width:66px">PART NUMBER</th><th style="width:68px">COLOUR TEMP</th><th style="width:83px">OUTPUT</th><th style="width:62px">POWER</th><th>INCLUDED GLOBES</th></tr>
    <tr><td class="thumb" rowspan="2"><span class="black" role="img" aria-label="Double spike light with globes"></span></td><td class="part">LX1425C</td><td>Cool white, 6000k</td><td>2x 300lm</td><td>12v LED 10w</td><td>2 x 5w LED globe</td></tr>
    <tr><td class="part">LX1425W</td><td>Warm white, 3000k</td><td>2x250lm</td><td>12v LED 10w</td><td>2 x 5w LED globe</td></tr>
  </table>

  <h1 class="back-title" style="left:282px;top:714px">MATT BLACK GARDEN SPIKE LIGHTS</h1>
  <ul class="specs" style="left:272px;top:766px">
    <li>single adjustable spike spotlight.</li><li>Aluminium poly poeder coated black.</li><li>Spike light : 285mm.</li><li>2m reinforced cable.</li><li>12v MR16 20w max.</li><li>IP rating : IP54.</li><li>Can be used with a halogen globe.</li><li>Refer to pages 188-192 for suitable LED drivers.</li>
  </ul>
  <div class="photo" role="img" aria-label="Single head black garden spike light" style="left:557px;top:755px;width:20px;height:148px;background:linear-gradient(180deg,#2a2a2a,#4a4a4a 25%,rgba(60,60,60,.5) 60%,rgba(238,240,243,0))"></div>

  <table class="spec-table" style="left:234px;top:907px;width:454px">
    <tr><th style="width:82px;text-align:center">IMAGE</th><th style="width:66px">PART NUMBER</th><th style="width:68px">COLOUR TEMP</th><th style="width:83px">OUTPUT</th><th style="width:62px">POWER</th><th>INCLUDED GLOBES</th></tr>
    <tr><td class="thumb" rowspan="2"><span class="black" role="img" aria-label="Single spike light with globe"></span></td><td class="part">LX1427C</td><td>Cool white, 6000k</td><td>300lm</td><td>12v LED 5w</td><td>5w LED globe</td></tr>
    <tr><td class="part">LX1427W</td><td>Warm white, 3000k</td><td>250lm</td><td>12v LED 5w</td><td>5w LED globe</td></tr>
  </table>

  <div class="contact">
    <h4>CONTACT US</h4>
    <p><svg width="9" height="11" viewBox="0 0 9 11"><path d="M4.5 0A4.3 4.3 0 0 0 .2 4.3C.2 7.5 4.5 11 4.5 11s4.3-3.5 4.3-6.7A4.3 4.3 0 0 0 4.5 0zm0 6a1.7 1.7 0 1 1 0-3.4 1.7 1.7 0 0 1 0 3.4z" fill="#fff"/></svg><span>Unit 8, 12-14 Harlow Street<br>Redfern, NSW 2016</span></p>
    <p><svg width="10" height="10" viewBox="0 0 10 10"><path d="M2 0l2 2.5-1.2 1.2a6 6 0 0 0 3.5 3.5L7.5 6 10 8 8.5 10C4 10 0 6 0 1.5z" fill="#fff"/></svg><span>02 9555 0142</span></p>
    <p><svg width="11" height="9" viewBox="0 0 11 9"><rect x=".5" y=".5" width="10" height="8" fill="none" stroke="#fff"/><path d="M.5.5l5 4 5-4" fill="none" stroke="#fff"/></svg><span>service@travik.com.au</span></p>
    <p><svg width="10" height="10" viewBox="0 0 10 10"><circle cx="5" cy="5" r="4.5" fill="none" stroke="#fff"/><path d="M.5 5h9M5 .5c-2.5 3-2.5 6 0 9M5 .5c2.5 3 2.5 6 0 9" fill="none" stroke="#fff" stroke-width=".8"/></svg><span>www.travik.com.au</span></p>
  </div>
</section>

</div>
</body>
</html>
```